WEB PAGES DESIGN

We need a web design for a new company called "NUBRA42". Our major business is that provide Internet Data Center solution, such as: rack/colocation, bandwidth, dedicated server, cloud server, CDN, and so on.
Requirements of Design:
1. Home page layout can refer to index-content.jpg in the attachments, but not limited.
2. According to match logo colors to design colors of web pages, Logo in the attachments.
3. The web contents of home page in image of the index-content.jpg.
4. The successful bidder will need to design three banner.
Industry/Entity Type
Business

```html
<!DOCTYPE html>
<html lang="en">
<head>
<meta charset="utf-8">
<title>NUBRA42 — Internet Data Solutions</title>
<link rel="stylesheet" href="https://fonts.googleapis.com/css2?family=Exo+2:wght@400;600;700&family=Michroma&family=Arimo:wght@400;700&display=swap">
<style>
:root{
  --green:#7dbb2f;
  --green-dark:#5e9421;
  --green-light:#9ad24a;
  --ink:#3a3a3a;
  --charcoal:#2b2a2d;
  --panel:#3a3a3a;
  --grey:#8b8b8b;
  --card:#e8e8e8;
  --white:#ffffff;
}
*{box-sizing:border-box;margin:0;padding:0}
html,body{width:1196px;height:1200px;overflow:hidden}
body{position:relative;background:var(--green);font-family:"Arimo",Arial,sans-serif;color:var(--ink)}
.abs{position:absolute}
.topbar{left:0;top:0;width:1196px;height:5px;background:#3d3d3d}
.header{left:0;top:5px;width:1196px;height:106px;background:linear-gradient(#fff 80%,#e6e6e6)}
.brand{left:198px;top:22px;display:flex;flex-direction:column;align-items:center;gap:6px}
.brand-mark{width:52px;height:52px;background:var(--green);border-radius:4px}
.brand-name{font:700 12px "Exo 2",sans-serif;color:#444;letter-spacing:1px}
.tagline{left:300px;width:528px;top:44px;text-align:center;font:700 27px "Exo 2",sans-serif;color:#444;letter-spacing:-.3px}
.tagline em{font-style:normal;color:var(--green)}
.inquiry{right:197px;top:36px;text-align:right}
.inquiry small{display:block;font-size:10.5px;color:#333}
.inquiry .phone{display:flex;align-items:center;gap:6px;font:700 22px "Exo 2",sans-serif;color:#333;margin-top:2px}
.nav{left:0;top:111px;width:1196px;height:40px;background:linear-gradient(var(--green-light),var(--green) 60%,var(--green-dark));border-bottom:3px solid #4d7a1b}
.nav a{position:absolute;top:13px;transform:translateX(-50%);font:11px "Michroma",sans-serif;color:#fff;text-decoration:none;white-space:nowrap}
.nav i{position:absolute;top:0;width:1px;height:37px;background:#4f801b}
.gap{left:0;top:151px;width:1196px;height:5px;background:#3b3b3b}
.hero{left:0;top:156px;width:1196px;height:294px;background:radial-gradient(circle at 40% 40%,#d9d9d9,#8a8a8a 60%,#5a5a5a)}
.hero-art{left:195px;top:175px;width:340px;height:275px;background:linear-gradient(90deg,#1d1d1d,#4a4a4a 50%,#1b1b1b)}
.hero-panel{left:730px;top:156px;width:296px;height:288px}
.hero-copy{left:730px;top:177px;width:296px;text-align:center;color:#e4e4e4}
.hero-copy h1{font:700 31px/1.02 "Exo 2",sans-serif;color:#f2f2f2}
.hero-copy p{font-size:12px;line-height:1.25;margin:12px 14px 0;color:#d6d6d6}
.btn{display:block;margin:16px auto 0;width:159px;height:28px;border-radius:3px;background:linear-gradient(var(--green-light),var(--green-dark));border:1px solid #b8e07f;font:600 12px/26px "Exo 2",sans-serif;color:#fff;text-decoration:none}
.core{left:0;top:450px;width:1196px;height:366px;background:#3a3a3a}
.core-frame{left:196px;top:467px;width:805px;height:336px;border-radius:10px;background:linear-gradient(#3c3c3c,#1e1e1e 60%,#0c0c0c);border:2px solid #111}
.core-title{left:196px;width:805px;top:463px;text-align:center;font:400 26px "Exo 2",sans-serif;color:#f0f0f0}
.core-title b{color:var(--green);font-weight:700}
.card{width:356px;height:108px;border-radius:8px;background:linear-gradient(120deg,#f2f2f2,#e1e1e1)}
.card .icon{position:absolute;left:22px;top:8px;width:74px;height:78px;border-radius:6px;background:linear-gradient(var(--green-light),var(--green-dark))}
.card h2{position:absolute;left:136px;top:21px;font:700 17px "Exo 2",sans-serif;color:var(--green);letter-spacing:.3px}
.card p{position:absolute;left:136px;top:45px;width:206px;font-size:10.5px;line-height:1.25;color:#333}
.partners-bg{left:0;top:816px;width:1196px;height:139px;background:#fff}
.partners-title{left:0;width:1196px;top:835px;text-align:center;font:700 10.5px "Exo 2",sans-serif;color:var(--green);letter-spacing:.5px}
.rule{left:245px;width:707px;height:1px;background:#e4e4e4}
.badge{top:872px;height:24px;border-radius:4px;background:#9a9a9a}
.footer{left:0;top:955px;width:1196px;height:179px;background:var(--green);color:#fff}
.footer h3{position:absolute;font:700 19px "Exo 2",sans-serif;color:#fff}
.news{left:186px;top:1025px;width:270px}
.news h4{font:700 13px "Exo 2",sans-serif}
.news p{font-size:10.5px;line-height:1.3;color:#eaf5d9;margin-top:3px}
.news a{display:block;margin-top:4px;font-size:10px;font-weight:700;color:#fff;text-decoration:none}
.foot-brand{left:505px;top:990px;display:flex;flex-direction:column;align-items:center;gap:8px}
.foot-brand .brand-mark{width:72px;height:72px;background:#fff}
.foot-brand .brand-name{color:#fff;font-size:14px}
.contact{left:666px;top:1022px;font-size:10.5px;line-height:1.5}
.contact .phone{display:flex;align-items:center;gap:5px;margin-top:3px;font:600 20px "Exo 2",sans-serif}
.chat{left:893px;top:1015px;display:flex;flex-direction:column;align-items:center;gap:8px}
.chat span{width:52px;height:52px;border-radius:50%;background:#fff}
.chat b{font:700 22px "Exo 2",sans-serif;color:#fff}
.legal{left:0;top:1134px;width:1196px;height:33px;background:#3a3a3a;color:#fff;font-size:9.5px}
.legal .copy{position:absolute;left:181px;top:11px}
.legal .links{position:absolute;right:189px;top:11px}
</style>
</head>
<body>
<div class="abs topbar"></div>

<header class="abs header"></header>
<div class="abs brand"><span class="brand-mark"></span><span class="brand-name">NUBRA42</span></div>
<div class="abs tagline">YOUR <em>INTERNET DATA</em> SOLUTIONS</div>
<div class="abs inquiry">
  <small>For Inquiries Contact us</small>
  <div class="phone">
    <svg width="24" height="24" viewBox="0 0 24 24"><circle cx="12" cy="12" r="10.5" fill="none" stroke="#333" stroke-width="1.6"/><path d="M8.5 6.5l2 2.3-1.1 1.4c.7 1.6 1.8 2.8 3.4 3.6l1.4-1.1 2.3 2-1.2 1.7c-3.8-.4-7.5-4.1-8-8z" fill="#333"/></svg>
    0-98-7654321
  </div>
</div>

<nav class="abs nav">
  <a href="#" style="left:268px">HOME</a><i style="left:324px"></i>
  <a href="#" style="left:428px">DEDICATED SERVER</a><i style="left:535px"></i>
  <a href="#" style="left:599px">HOSTING</a><i style="left:664px"></i>
  <a href="#" style="left:752px">DATA CENTERS</a><i style="left:843px"></i>
  <a href="#" style="left:912px">ABOUT US</a>
</nav>
<div class="abs gap"></div>

<div class="abs hero" role="img" aria-label="Grey data-centre backdrop with digits and hexagon patterns"></div>
<div class="abs hero-art" role="img" aria-label="Three black server towers with glowing green stripes"></div>
<svg class="abs hero-panel" viewBox="0 0 296 288"><polygon points="0,0 296,0 296,224 148,288 0,224" fill="#2b2a2d"/></svg>
<div class="abs hero-copy">
  <h1>IDC<br>SOLUTIONS</h1>
  <p>NUBRA42 provides a wide range of highly specialized solutions that utilizes technology to transform your organization.</p>
  <a class="btn" href="#">read more</a>
</div>

<section class="abs core"></section>
<div class="abs core-frame"></div>
<div class="abs core-title">Get <b>NUBRA42</b> Core Technologies</div>

<div class="abs card" style="left:224px;top:545px">
  <div class="icon" role="img" aria-label="Green dedicated server icon"></div>
  <h2>DEDICATED SERVERS</h2>
  <p>Consectetur adipisicing elit, sed do eiusmod tempor incididunt ut labore et dolore magna aliqua. Ut enim ad minim veniam.</p>
</div>
<div class="abs card" style="left:611px;top:545px">
  <div class="icon" role="img" aria-label="Green hard drive icon"></div>
  <h2>HOSTING SERVERS</h2>
  <p>Sed ut perspiciatis, unde omnis ise natus error sit voluptatem accusantium doloremque laudantium, totam rem.</p>
</div>
<div class="abs card" style="left:224px;top:670px">
  <div class="icon" role="img" aria-label="Green server rack icon"></div>
  <h2>RACK &amp; BANDWIDTH</h2>
  <p>Nemo enim ipsam voluptaem, quia voluptas sit, aspernatur aut odit aut fugit, sed quia consequuntur magni dolores eos.</p>
</div>
<div class="abs card" style="left:611px;top:670px">
  <div class="icon" role="img" aria-label="Green handshake icon"></div>
  <h2 style="left:139px;top:16px">RESELLER &amp; REFERRAL</h2>
  <p style="left:139px;top:40px">Et harum quidem rerum facilis est et expedita distinctio. Nam libero tempore, cum soluta nobis est eligendi optio.</p>
</div>

<section class="abs partners-bg"></section>
<div class="abs partners-title">OUR TRUSTED PARTNERS</div>
<div class="abs rule" style="top:853px"></div>
<div class="abs rule" style="top:905px"></div>
<svg class="abs" style="left:191px;top:868px" width="20" height="34" viewBox="0 0 20 34"><polygon points="20,0 20,34 0,17" fill="#b5b5b5"/></svg>
<svg class="abs" style="left:988px;top:868px" width="20" height="34" viewBox="0 0 20 34"><polygon points="0,0 0,34 20,17" fill="#b5b5b5"/></svg>
<div class="abs badge" style="left:245px;width:68px"></div>
<div class="abs badge" style="left:331px;width:92px"></div>
<div class="abs badge" style="left:444px;width:108px"></div>
<div class="abs badge" style="left:572px;width:98px"></div>
<div class="abs badge" style="left:688px;width:92px"></div>
<div class="abs badge" style="left:796px;width:68px"></div>
<div class="abs badge" style="left:878px;width:74px"></div>

<footer class="abs footer">
  <h3 style="left:184px;top:32px">LATEST NEWS</h3>
  <h3 style="left:666px;top:29px">CONTACT US</h3>
</footer>
<div class="abs news">
  <h4>Lorem ipsum dolor sit amet, consectetur</h4>
  <p>Elit, sed do eiusmod tempor incididunt ut labore et dolore magna aliqua. Ut enim ad minim veniam, quis nostrud ...</p>
  <a href="#">read more +</a>
</div>
<div class="abs foot-brand"><span class="brand-mark"></span><span class="brand-name">NUBRA42</span></div>
<div class="abs contact" style="color:#fff">
  5678 Harbor Lane Suite 9<br>
  Lakeview City 204310<br>
  <span style="font-size:11.5px">info@NUBRA42.com</span>
  <div class="phone">
    <svg width="22" height="22" viewBox="0 0 24 24"><circle cx="12" cy="12" r="10.5" fill="none" stroke="#fff" stroke-width="1.6"/><path d="M8.5 6.5l2 2.3-1.1 1.4c.7 1.6 1.8 2.8 3.4 3.6l1.4-1.1 2.3 2-1.2 1.7c-3.8-.4-7.5-4.1-8-8z" fill="#fff"/></svg>
    0-98-7654321
  </div>
</div>
<div class="abs chat"><span></span><b>TalkWave</b></div>

<div class="abs legal">
  <span class="copy">© Copyright 2014 NUBRA42 Consulting. All Rights Reserved.</span>
  <span class="links">Terms of Service &nbsp;|&nbsp; Privacy Policy &nbsp;|&nbsp; Contact Us</span>
</div>
</body>
</html>
```